Business cards - ZELTO Roofing & Siding

We need simple business cards made up for our Roofing & Siding business based in Calgary Alberta.
The logo on one side of the card and potentially our slogan "Built with trust, verified by time".
The other side could have:
-A small logo
-Rep name:
-Rep cell phone:
-Rep email:
-Office phone: 403-688-2904
-Website: PrairieTopCrafters.com

We would like to incorporate the colours from our logo, especially the lite blue on the jpeg file. I have attached the ai file and jpeg file. We like the colours better on the jpeg file.

```html
<!DOCTYPE html>
<html lang="en">
<head>
<meta charset="utf-8">
<title>ZELTO Roofing &amp; Siding – Business Cards</title>
<link rel="stylesheet" href="https://fonts.googleapis.com/css2?family=Arimo:wght@400;700&family=Montserrat:wght@500;600&display=swap">
<style>
  :root {
    --backdrop: #e4e4e2;
    --card-white: #ffffff;
    --brand-red: #ec1f26;
    --brand-blue: #4080c4;
    --brand-blue-deep: #0b66b2;
    --ink: #111111;
    --ink-soft: #555555;
    --card-dark: #323232;
    --card-dark-edge: #262626;
    --on-dark: #ffffff;
  }
  * { margin: 0; padding: 0; box-sizing: border-box; }
  html, body {
    width: 1200px; height: 801px; overflow: hidden;
    background: var(--backdrop);
  }
  .sheet {
    position: relative; width: 1200px; height: 801px;
    display: flex; align-items: center; justify-content: center; gap: 40px;
  }
  .card {
    position: relative; width: 540px; height: 309px; overflow: hidden;
    box-shadow: 0 6px 18px rgba(0,0,0,0.18);
  }

  /* Front card */
  .card--front { background: var(--card-white); }
  .card__bands { position: absolute; inset: 0; }
  .brand-name {
    position: absolute; left: 34px; top: 52px;
    font-family: "Montserrat", sans-serif; font-weight: 600;
    color: var(--ink); line-height: 1;
  }
  .brand-name__word { display: block; font-size: 62px; letter-spacing: 6px; }
  .brand-name__line { display: block; font-size: 17px; letter-spacing: 5.5px; margin-top: 8px; }
  .rep {
    position: absolute; right: 34px; top: 30px; text-align: right;
    font-family: "Arimo", sans-serif;
  }
  .rep__name { font-weight: 700; font-size: 17px; color: var(--brand-red); letter-spacing: 0.3px; }
  .rep__title { font-size: 13px; color: var(--ink-soft); margin-top: 2px; }
  .contact {
    position: absolute; left: 24px; bottom: 20px; list-style: none;
    font-family: "Arimo", sans-serif; font-size: 14.5px; color: var(--on-dark);
  }
  .contact__item { display: flex; align-items: center; gap: 9px; height: 21px; }
  .contact__icon { width: 14px; height: 14px; flex: none; }

  /* Back card */
  .card--back {
    display: flex; flex-direction: column; align-items: center; justify-content: center;
  }
  .card__texture {
    position: absolute; inset: 0;
    background: linear-gradient(135deg, var(--card-dark-edge) 0%, var(--card-dark) 45%, #3e3e3e 100%);
  }
  .back-mark {
    position: relative; text-align: center;
    font-family: "Montserrat", sans-serif; font-weight: 500; color: var(--on-dark);
  }
  .back-mark__est { font-size: 13px; letter-spacing: 2px; margin-bottom: 6px; }
  .back-mark__word { font-size: 58px; letter-spacing: 7px; line-height: 1; }
  .back-mark__line { font-size: 15px; letter-spacing: 5px; margin-top: 8px; }
  .back-mark__square {
    width: 14px; height: 14px; background: var(--brand-blue);
    margin: 0 auto 12px;
  }
</style>
</head>
<body>
<main class="sheet">

  <section class="card card--front" aria-label="Business card front">
    <svg class="card__bands" viewBox="0 0 540 309" preserveAspectRatio="none" aria-hidden="true">
      <polygon points="0,230 360,230 300,309 0,309" fill="var(--brand-red)"/>
      <polygon points="0,170 395,170 410,150 0,150" fill="none"/>
      <polygon points="380,309 455,200 540,200 540,240 478,240 426,309" fill="var(--brand-blue)"/>
      <polygon points="320,309 372,230 392,230 340,309" fill="var(--brand-blue-deep)"/>
    </svg>

    <div class="brand-name">
      <span class="brand-name__word">ZELTO</span>
      <span class="brand-name__line">ROOFING &amp; SIDING</span>
    </div>

    <div class="rep">
      <p class="rep__name">MARCUS DELANE</p>
      <p class="rep__title">Manager</p>
    </div>

    <ul class="contact">
      <li class="contact__item">
        <svg class="contact__icon" viewBox="0 0 14 14" aria-hidden="true"><rect x="3.5" y="1" width="7" height="12" rx="1.2" fill="none" stroke="#fff" stroke-width="1.3"/><line x1="6" y1="11" x2="8" y2="11" stroke="#fff" stroke-width="1.1"/></svg>
        <span>403-688-2904</span>
      </li>
      <li class="contact__item">
        <svg class="contact__icon" viewBox="0 0 14 14" aria-hidden="true"><path d="M3 1.5 L5.2 1.5 L6 4.3 L4.6 5.4 C5.4 7.1 6.9 8.6 8.6 9.4 L9.7 8 L12.5 8.8 L12.5 11 C12.5 11.9 11.8 12.5 10.9 12.5 C6 12.2 1.8 8 1.5 3.1 C1.5 2.2 2.1 1.5 3 1.5 Z" fill="#fff"/></svg>
        <span>403-688-2904</span>
      </li>
      <li class="contact__item">
        <svg class="contact__icon" viewBox="0 0 14 14" aria-hidden="true"><rect x="1" y="3" width="12" height="8.5" fill="#fff"/><polyline points="1,3 7,8 13,3" fill="none" stroke="var(--brand-red)" stroke-width="1.2"/></svg>
        <span>info@PrairieTopCrafters.com</span>
      </li>
      <li class="contact__item">
        <svg class="contact__icon" viewBox="0 0 14 14" aria-hidden="true"><circle cx="7" cy="7" r="6" fill="#fff"/><ellipse cx="7" cy="7" rx="2.6" ry="6" fill="none" stroke="var(--brand-red)" stroke-width="1"/><line x1="1" y1="7" x2="13" y2="7" stroke="var(--brand-red)" stroke-width="1"/></svg>
        <span>PrairieTopCrafters.com</span>
      </li>
    </ul>
  </section>

  <section class="card card--back" aria-label="Business card back">
    <div class="card__texture" role="img" aria-label="Dark charcoal background with a repeated embossed company pattern"></div>
    <div class="back-mark">
      <div class="back-mark__square" aria-hidden="true"></div>
      <p class="back-mark__est">Est. 1991</p>
      <p class="back-mark__word">ZELTO</p>
      <p class="back-mark__line">ROOFING &amp; SIDING</p>
    </div>
  </section>

</main>
</body>
</html>
```